Powerpoint template for basic scientists studying immunology

We are an QFB-funded consortium of basic science researchers at academic centers in Boston, Philadelphia and Oxford, UK. We study why the immune system fails to get rid of Hepatitis C virus, and whether new antiviral treatments that reduce viral load improve immune function. We are looking for a powerpoint template that we can use as a "brand" for our research consortium. It would feature a logo (file attached) and should represent the fonts/colors contained in the logo. We we would present at meetings and to program officers at the QFB, but, if we ever get around to it, would also be on a website.

The scientific description is as follows:
Hepatitis C virus (HCV) infects 185 million persons worldwide, is the leading indication for liver transplantation and, in the US, has a higher mortaliy rate than HIV. The annual healthcare costs associated with HCV exceed $9 billion, a number expected to increase as the epidemic matures and end stage liver disease peaks over the next decade. By virtue of its remarkable predilection for persistence, HCV is a model chronic viral infection. Mounting evidence supports the idea that HCV, while inducing type I IFN expression, maintains chronicity by virtue of global suppression of host innate and adaptive immunity. The mainstay of treatment for the last two decades, IFN-α-based regimens are ineffective in many patient subgroups and have significant side effects. The recent development of highly effective direct acting antivirals (DAA) against HCV promises to alter the landscape of this devastating infection by offering curative therapy without IFN. However, it remains essential that we understand what type of immunity remains following pharmacological eradication of the virus because: a) many HCV infected subjects remain at risk for re-infection; and b) DAAs are only partially effective in some patient subgroups, particularly those with past treatment with IFN. The imminent availability of IFN-free treatment for HCV offers an unprecedented opportunity to understand broad questions about alterations in immunity in humans with cure of chronic infections. Until now, mechanistic dissection of human immune responses has been challenging due to limited ability to directly perturb the system. The organizing principle of this U19 Program therefore, is to capitalize on the unique opportunity to, for the first time, cure chronic viral infection in humans without immune modulation and interrogate the immunological changes that ensue. Thus, we have formulated the following central hypothesis for this Program: DAA-mediated cure of chronic HCV infection will lead to partial "resetting" of some immune abnormalities, but specific immunological defects will persist in some subjects that prevent development of optimal immunity to HCV. We will test this hypothesis through a set of integrated Projects and Cores.

Target Market(s)

scientists.

Industry/Entity Type

Biotechnology

Font styles to use
Sans Serif

Requirements
Must have
• Very clean, very simple. Mostly whitespace for puting graphs and data on. Colors, fonts should match the logo. Please see ppt example.
Should not have
• too much of the ppt covered with the logo.

```html
<!DOCTYPE html>
<html lang="en">
<head>
<meta charset="utf-8">
<title>KELVIN HRC Consortium – Slide Template</title>
<link href="https://fonts.googleapis.com/css2?family=Arimo:wght@400;700&display=swap" rel="stylesheet">
<style>
  :root {
    --stage: #000000;
    --slide: #ffffff;
    --brand-blue: #1a9ad6;
    --brand-green: #6cbf3c;
    --ink: #1e1e1e;
    --muted: #8a8a8a;
    --badge: #8c8c8c;
    --rule: #333333;
    --pattern: #ececec;
  }
  * { box-sizing: border-box; margin: 0; padding: 0; }
  html, body {
    width: 924px; height: 1200px; overflow: hidden;
    background: var(--stage);
    font-family: "Arimo", Arial, sans-serif;
    color: var(--ink);
  }
  .canvas { position: relative; width: 924px; height: 1200px; }
  .slide {
    position: absolute;
    width: 752px; height: 564px;
    background: var(--slide);
    overflow: hidden;
  }
  .slide--agenda { left: 90px; top: 24px; }
  .slide--about  { left: 88px; top: 604px; width: 750px; height: 562px; }

  .corner-pattern {
    position: absolute; right: 0; top: 0;
    width: 226px; height: 226px;
    background: radial-gradient(circle at 85% 20%, var(--pattern) 0%, #f5f5f5 45%, rgba(255,255,255,0) 75%);
  }
  .header-bar {
    position: absolute; left: 86px; top: 0;
    width: 4px; height: 63px;
    background: var(--brand-green);
  }
  .header-title {
    position: absolute; left: 102px; top: 26px;
    font-size: 15px; color: var(--brand-green); letter-spacing: 0.2px;
  }
  .header-date {
    position: absolute; left: 102px; top: 45px;
    font-size: 15px; font-weight: 700; color: var(--ink);
  }
  .page-badge {
    position: absolute; left: 692px; top: 20px;
    width: 44px; height: 44px;
  }
  .page-badge text {
    font-family: "Arimo", Arial, sans-serif;
    font-size: 16px; fill: #ffffff;
  }
  .slide-title {
    position: absolute; left: 83px; top: 116px;
    font-size: 39px; font-weight: 700; color: var(--brand-blue);
  }
  .agenda-list {
    position: absolute; left: 102px; top: 209px;
    list-style: none;
    font-size: 13.5px; line-height: 16.6px;
  }
  .agenda-list li { position: relative; margin-bottom: 16.6px; }
  .agenda-list li::before {
    content: ""; position: absolute; left: -21px; top: 4px;
    width: 9px; height: 9px; border-radius: 50%;
    background: var(--brand-green);
  }
  .about-text {
    position: absolute; left: 86px; top: 211px;
    width: 590px;
    font-size: 12.2px; line-height: 15px; letter-spacing: -0.1px;
  }
  .about-text .tail { margin-top: 6px; }
  .footer-rule {
    position: absolute; left: 86px; top: 515px;
    width: 528px; height: 1px; background: var(--rule);
  }
  .footer-copy {
    position: absolute; left: 86px; top: 520px;
    font-size: 10px; color: var(--ink);
  }
  .brand-mark {
    position: absolute; left: 606px; top: 466px;
    width: 116px; text-align: center;
  }
  .brand-dot {
    display: block; margin: 0 auto 12px;
    width: 26px; height: 26px; border-radius: 50%;
    background: var(--brand-blue);
  }
  .brand-name {
    display: block;
    font-size: 14px; line-height: 16px; color: var(--muted);
    letter-spacing: 0.2px; white-space: nowrap;
  }
</style>
</head>
<body>
<main class="canvas">

  <section class="slide slide--agenda">
    <div class="corner-pattern" role="img" aria-label="Faint grey hexagon background pattern"></div>
    <div class="header-bar"></div>
    <p class="header-title">PPT HEADING GOES HERE</p>
    <p class="header-date">JUNE,2015</p>
    <svg class="page-badge" viewBox="0 0 44 44">
      <polygon points="11,3 33,3 44,22 33,41 11,41 0,22" fill="var(--badge)"/>
      <text x="22" y="28" text-anchor="middle">02</text>
    </svg>
    <h1 class="slide-title">Agenda</h1>
    <ul class="agenda-list">
      <li>US Corporation with 16 years Lease and Loan Management Software<br>experience US Corporation with 16 years Lease and Loan Management<br>Software experience</li>
      <li>US Corporation with 16 years Lease and Loan Management Software<br>experience US Corporation with 16 years Lease and L</li>
      <li>US Corporation with 16 years Lease and</li>
      <li>US Corporation with 16 years Lease and Loan Management Software<br>experience US Corporation with 16 y</li>
      <li>US Corporation with 16 years Lease and</li>
    </ul>
    <div class="footer-rule"></div>
    <p class="footer-copy">© 2015 KELVIN HRC CONSORTIUM</p>
    <div class="brand-mark">
      <span class="brand-dot"></span>
      <span class="brand-name">KELVIN HRC</span>
    </div>
  </section>

  <section class="slide slide--about">
    <div class="corner-pattern" role="img" aria-label="Faint grey hexagon background pattern"></div>
    <div class="header-bar"></div>
    <p class="header-title">PPT HEADING GOES HERE</p>
    <p class="header-date">JUNE,2015</p>
    <svg class="page-badge" viewBox="0 0 44 44">
      <polygon points="11,3 33,3 44,22 33,41 11,41 0,22" fill="var(--badge)"/>
      <text x="22" y="28" text-anchor="middle">03</text>
    </svg>
    <h1 class="slide-title">About Us</h1>
    <div class="about-text">
      <p>Organizations gain comprehensive visibility into and control over devices accessing their corporate<br>network so they can quickly identify and address suspicious activity on the network that could lead to<br>potential threats like data breaches. Our technology helps organizations gain comprehensive visibility<br>into and control over devices accessing their corporate network so they can quickly identify and address<br>suspicious activity on the network that could lead to potential threats like data breaches. Our technology<br>helps organizations gain comprehensive visibility into and control over devices accessing their<br>corporate network so they can quickly identify and address suspicious activity on the network that could<br>lead to potential threats like data breaches.<br>and control over devices accessing their corporate network so they can quickly identify and address<br>suspicious activity on the network that could lead to potential threats like data breaches.<br>Our technology helps organizations gain comprehensive visibility into and control over devices<br>accessing their corporate network so they can quickly identify and address suspicious activity on the<br>network that could lead to potential threats like data breaches. Our technology helps organizations gain</p>
      <p class="tail">comp</p>
    </div>
    <div class="footer-rule"></div>
    <p class="footer-copy">© 2015 KELVIN HRC CONSORTIUM</p>
    <div class="brand-mark">
      <span class="brand-dot"></span>
      <span class="brand-name">KELVIN HRC</span>
    </div>
  </section>

</main>
</body>
</html>
```